WedlockForge USA needs a Prayer booklet

I need a bookmark 2.5 x 8.5, full color, 2-sided, that lists a number of questions for married couples to ask themselves. The numbering is a little mixed up. Please make it look good.
My layout started with a different idea, but now would like it to be the shape of a larger bookmark.

Target Market(s)

Church

```html
<!DOCTYPE html>
<html lang="en">
<head>
<meta charset="utf-8">
<title>An Examination of Conscience for the Married — WedlockForge USA Bookmark</title>
<link rel="stylesheet" href="https://fonts.googleapis.com/css2?family=Open+Sans:wght@600;700;800&display=swap">
<style>
  :root {
    --backdrop: #e8e5e1;
    --ink: #141414;
    --plum: #3a1c5c;
    --violet: #4a2470;
    --rose-line: #e7a9cf;
    --brand-blue: #1d4f9a;
  }
  * { margin: 0; padding: 0; box-sizing: border-box; }
  html, body { width: 960px; height: 1200px; overflow: hidden; }
  body {
    background: var(--backdrop);
    font-family: "Open Sans", Arial, sans-serif;
    color: var(--ink);
    position: relative;
  }

  /* Bookmark sides: 2.5 x 8.5 in ratio */
  .bookmark {
    position: absolute; top: 56px; width: 320px; height: 1088px;
    overflow: hidden; display: flex; flex-direction: column;
  }
  .bookmark--front { left: 140px; }
  .bookmark--back { left: 500px; }

  .bookmark-bg { position: absolute; inset: 0; z-index: 0; }
  .bookmark--front .bookmark-bg {
    background: linear-gradient(180deg, rgba(255,255,255,0) 0%, rgba(255,255,255,0) 44%, #eceef1 46%, #f1ede8 70%, #f3ecdf 100%);
  }
  .bookmark--back .bookmark-bg {
    background: radial-gradient(ellipse at 40% 78%, rgba(236,214,200,.5), rgba(236,214,200,0) 50%),
                linear-gradient(180deg, #f4eee3 0%, #f1ede8 50%, #f6f6f7 62%, #eef0f2 100%);
  }
  .bookmark > *:not(.bookmark-bg) { position: relative; z-index: 1; }

  /* Front */
  .cover {
    position: relative; height: 500px; flex: none;
    padding: 150px 34px 0 30px;
  }
  .beach-photo {
    position: absolute; inset: 0;
    background: radial-gradient(circle at 84% 40%, #fff6c8 0%, rgba(255,236,170,.6) 14%, rgba(255,236,170,0) 38%),
                linear-gradient(180deg, #f7f1e4 0%, #f2e6c8 40%, #dfd8cf 60%, #cfd1d4 80%, #e6e3e2 100%);
  }
  .rose-rule-h { position: absolute; left: 0; top: 26px; width: 320px; height: 9px; background: var(--rose-line); opacity: .8; }
  .rose-rule-v { position: absolute; left: 290px; top: 0; width: 8px; height: 500px; background: var(--rose-line); opacity: .8; }
  .cover-title {
    position: relative;
    font-size: 27px; font-weight: 800; line-height: 35px; color: var(--plum); letter-spacing: .2px;
  }
  .cover .question-list { position: relative; margin-top: 60px; width: 240px; }

  .question-list {
    list-style: none;
    font-size: 12px; font-weight: 600; line-height: 15.5px;
  }
  .question-list li { padding-left: 19px; text-indent: -19px; margin-bottom: 5px; }
  .front-questions { padding: 10px 30px 0 30px; }

  /* Back */
  .back-questions { padding: 44px 30px 0 30px; }
  .blank-line { display: inline-block; width: 180px; border-bottom: 1.2px solid var(--ink); margin-left: 6px; }
  .prayer-title {
    margin-top: 22px; text-align: center;
    font-size: 14px; font-weight: 700; color: var(--violet); font-variant: small-caps; letter-spacing: .3px;
  }
  .prayer-title span { border-bottom: 1.5px solid var(--violet); }
  .prayer-text {
    margin-top: 8px; padding: 0 22px; text-align: center;
    font-size: 12.5px; font-weight: 600; line-height: 19px;
  }
  .brand {
    margin-top: 30px; display: flex; justify-content: center; align-items: center; gap: 10px;
  }
  .brand-mark { width: 28px; height: 28px; background: var(--brand-blue); }
  .brand-name { font-size: 18px; font-weight: 700; color: var(--brand-blue); }
  .order-info {
    margin-top: 34px; text-align: center;
    font-size: 11.5px; font-weight: 700; line-height: 15.5px;
  }
  .order-info .web { color: var(--violet); }
</style>
</head>
<body>

<section class="bookmark bookmark--front" aria-label="Bookmark front">
  <div class="bookmark-bg" role="img" aria-label="Soft photo of a woman in prayer with folded hands in warm light"></div>
  <div class="cover">
    <div class="beach-photo" role="img" aria-label="Photo of a couple embracing on a beach at sunset"></div>
    <div class="rose-rule-h"></div>
    <div class="rose-rule-v"></div>
    <h1 class="cover-title">AN EXAMINATION<br>OF CONSCIENCE<br>FOR THE<br>MARRIED</h1>
    <ol class="question-list">
      <li>1. Have I said thoughtless or hurtful words, yelled indiscriminately, or in any other way been unkind or uncharitable to my spouse or family members?</li>
    </ol>
  </div>
  <ol class="question-list front-questions">
    <li>2. Have I been angry at spouse?</li>
    <li>3. Have I allowed resentments and bitterness toward my spouse to take root in my mind?</li>
    <li>4. Has pride or selfishness caused me to stumble and fall short in my marriage?</li>
    <li>5. Do I have an attitude that I’m right and my spouse is always wrong?</li>
    <li>6. Have I been hard-hearted or callous?</li>
    <li>7. Have I been unfair, causing pain, resentment and hurt in my marriage?</li>
    <li>8. Are my priorities misplaced?</li>
    <li>9. Am I defensive or critical of my spouse, of my children?</li>
    <li>10. Have I been rude or self-seeking?</li>
    <li>11. Do I keep a record of wrongs?</li>
    <li>12. Have I been unsupportive?</li>
    <li>13. Have I spoken sharply or sarcastically to my spouse? Have I spoken in a demeaning or negative way?</li>
  </ol>
</section>

<section class="bookmark bookmark--back" aria-label="Bookmark back">
  <div class="bookmark-bg" role="img" aria-label="Soft photo of a couple holding hands with a wedding ring"></div>
  <ol class="question-list back-questions">
    <li>14. Have I failed to seek God’s plan for our marriage?</li>
    <li>15. Has infidelity, pornography, overspending occurred?</li>
    <li>16. Have I failed to follow the teachings of the Church on Family Planning?</li>
    <li>17. Have I failed to turn to God in prayer?</li>
    <li>18. Have I been unwilling to work to make our marriage healthy?</li>
    <li>19. Have I failed to protect my spouse?</li>
    <li>20. Have I been unwilling to make changes in my behavior? In my attitude? If so, what has been the consequences?</li>
    <li>21. Have I threatened to leave? Or avoided the problems I create?</li>
    <li>22. Have I told little lies, or big ones? Been imprecise in my words?</li>
    <li>23. Am I impatient with the ones I love?</li>
    <li>24. Have I physically abused my spouse?</li>
    <li>25. Have I gossiped about my spouse?</li>
    <li>26. Have I failed to seek forgiveness?</li>
    <li>27. Have I been unforgiving?</li>
    <li>28.<span class="blank-line"></span></li>
  </ol>
  <h2 class="prayer-title"><span>Act of Contrition</span></h2>
  <p class="prayer-text">
    O my God, I am heartily sorry for having offended you. And I detest all my sins because of your just punishment. But most of all because they offend you, my God, who art all-good and deserving of all my love. I firmly resolve, with the help of your grace, to sin no more, and to avoid the near occasion of sin. Amen.
  </p>
  <div class="brand">
    <span class="brand-mark"></span>
    <span class="brand-name">WedlockForge USA</span>
  </div>
  <p class="order-info">
    Additional quantity copies of<br>
    AN EXAMINATION OF CONSCIENCE<br>
    FOR THE MARRIED are available from<br>
    <span class="web">www.wedlockforgeusa.org or</span><br>
    by contacting Dan &amp; Laurie Hollis at<br>
    &#9990; (555) 014-0237.
  </p>
</section>

</body>
</html>
```